Business Card Design Project

Basketball Training program

Offers: Travel Club Program - Camps - Clinics - Private Training

website: rivetbasketball.example
Phone Contact: Main Phone: 555-317-4826
Email: rivet.basketball@mailbox.example

Industry/Entity Type

Business

Contact Information for Business Card

Need one for the following coaches:
Marlo Quintrell - Boys & Girls Basketball Coach
Noweni Tasker - Girls Basketball Coach
Anselmo Duvray - Director/Head Coach
Hollis Ruk- Boys Basketball
Warren Olivash - Boys Basketball
Tomas Ferlanga - Boys Basketball
Kavin Sotherby- Boys Basketball/ Trainer
Al Varnock - Boys & Girls Basketball Coach

Basketball Training program Logo - one side

Logo on the corner
new one on the left (RB)
old one on the right (old one is with the rivet and basketball)

```html
<!DOCTYPE html>
<html lang="en">
<head>
<meta charset="UTF-8">
<title>Rivet Basketball – Business Card</title>
<link rel="stylesheet" href="https://fonts.googleapis.com/css2?family=Open+Sans:wght@400;600;700;800&display=swap">
<style>
  :root {
    --stage: #2b2b2d;
    --card-white: #ffffff;
    --ink: #111111;
    --ink-soft: #2a2a2a;
    --gold: #f5b21b;
    --band: #0c0c0c;
    --light: #f4f4f4;
  }
  * { box-sizing: border-box; margin: 0; padding: 0; }
  html, body { width: 1200px; height: 900px; overflow: hidden; }
  body {
    background: var(--stage);
    font-family: "Open Sans", Arial, sans-serif;
    position: relative;
  }
  .card {
    position: absolute;
    left: 290px;
    width: 620px;
    height: 354px;
    border-radius: 26px;
    overflow: hidden;
    background: var(--card-white);
    box-shadow: 0 14px 30px rgba(0,0,0,0.45);
  }
  .card--front { top: 70px; }
  .card--back { top: 476px; }

  /* Front */
  .brand {
    display: flex;
    align-items: center;
    gap: 12px;
    font-weight: 800;
    color: var(--ink);
    text-transform: uppercase;
    line-height: 1;
  }
  .brand__dot {
    border-radius: 50%;
    background: var(--gold);
    flex: none;
  }
  .card--front .brand {
    position: absolute;
    left: 50%;
    top: 120px;
    transform: translateX(-50%);
    font-size: 40px;
    letter-spacing: 1px;
    white-space: nowrap;
  }
  .card--front .brand__dot { width: 44px; height: 44px; }
  .services {
    position: absolute;
    left: 0; right: 0;
    top: 268px;
    text-align: center;
    font-size: 15px;
    color: var(--ink-soft);
    letter-spacing: 0.3px;
  }

  /* Back */
  .back-shapes { position: absolute; inset: 0; }
  .monogram {
    position: absolute;
    left: 38px;
    top: 44px;
    display: flex;
    align-items: center;
    gap: 10px;
    font-size: 64px;
    font-weight: 800;
    color: var(--ink);
    line-height: 1;
  }
  .monogram__ring {
    width: 26px; height: 26px;
    border-radius: 50%;
    background: var(--ink);
  }
  .card--back .brand {
    position: absolute;
    right: 30px;
    top: 36px;
    font-size: 22px;
    gap: 8px;
  }
  .card--back .brand__dot { width: 24px; height: 24px; }
  .contact {
    position: absolute;
    right: 26px;
    top: 176px;
    list-style: none;
    text-align: right;
    font-size: 14px;
    color: var(--gold);
    line-height: 1.35;
  }
  .contact li { display: flex; justify-content: flex-end; align-items: center; gap: 7px; }
  .contact svg { width: 11px; height: 11px; fill: none; stroke: var(--light); stroke-width: 2; }
  .coach {
    position: absolute;
    left: 38px;
    bottom: 34px;
  }
  .coach__name {
    font-size: 25px;
    font-weight: 700;
    color: var(--gold);
    letter-spacing: 0.5px;
  }
  .coach__role {
    font-size: 14px;
    color: var(--light);
  }
</style>
</head>
<body>
  <section class="card card--front">
    <div class="brand"><span class="brand__dot"></span>Rivet Basketball</div>
    <p class="services">Travel Club Program - Camps - Clinics - Private Training</p>
  </section>

  <section class="card card--back">
    <svg class="back-shapes" viewBox="0 0 620 354" preserveAspectRatio="none" aria-hidden="true">
      <path d="M0,246 C260,236 500,150 588,0 L620,0 L620,354 L0,354 Z" fill="var(--gold)"/>
      <path d="M0,258 C270,246 520,160 620,26 L620,354 L0,354 Z" fill="var(--band)"/>
    </svg>

    <div class="monogram"><span class="monogram__ring"></span>RB</div>
    <div class="brand"><span class="brand__dot"></span>Rivet Basketball</div>

    <ul class="contact">
      <li>555-317-4826
        <svg viewBox="0 0 24 24"><path d="M5 3h4l2 5-3 2a12 12 0 0 0 6 6l2-3 5 2v4a2 2 0 0 1-2 2A18 18 0 0 1 3 5a2 2 0 0 1 2-2z"/></svg>
      </li>
      <li>rivet.basketball@mailbox.example
        <svg viewBox="0 0 24 24"><rect x="3" y="5" width="18" height="14"/><path d="M3 6l9 7 9-7"/></svg>
      </li>
      <li>rivetbasketball.example
        <svg viewBox="0 0 24 24"><circle cx="12" cy="12" r="9"/><path d="M3 12h18M12 3c3 3 3 15 0 18M12 3c-3 3-3 15 0 18"/></svg>
      </li>
    </ul>

    <div class="coach">
      <p class="coach__name">Anselmo Duvray</p>
      <p class="coach__role">Director/Head Coach</p>
    </div>
  </section>
</body>
</html>
```